Pelorn.com- International Goal Achievement Coach Needs Website Design

I need a web design for my new company called Pelorn. I help people who are stuck, people who have a big dream, but don't know how to get there. I help them to break their dreams down into small, manageable steps... and then I'm the "kick in the shin" to get them moving and thriving!

We can all be better- We can all DO better. I inspire people to Go Boldly in the direction of your dreams.

I have uploaded my logo along with some vintage champagne posters. Please use the vintage posters as inspiration. I like the bold, vintage look and feel. I would love the main colors of the design to be black, white and metallic gold. And to follow along this vintage look and feel. Please feel free to use the logo in black or metallic gold or white.

Target Market(s)

websites that I like- lucindavarek.com & tessaw.tv

I would like to also use the vintage champagne photos attached as inspiration as well.

Industry/Entity Type

It Company

Requirements
Must have
• Tabs should include: About, Work With Me, Praise, Giving Back

On the homepage add:
* Sign up for newsletter with space to enter name and email (No click throughs)
* Upcoming Events/Sessions
* Newsletter Posts
* Resources
* Praise Section

* Large photo on top with additional photos throughout the page/site.
Nice to have
• Any additions you can bring to the table would be greatly appreciated.

```html
<!DOCTYPE html>
<html lang="en">
<head>
<meta charset="utf-8">
<title>Pelorn — Goal Achievement Coaching</title>
<link href="https://fonts.googleapis.com/css2?family=Cabin:wght@400;500;600&family=Open+Sans:wght@400;600;700&family=Libre+Baskerville&display=swap" rel="stylesheet">
<style>
:root{
  --gold:#a97c4f;
  --gold-light:#c39a6b;
  --dark:#262626;
  --darker:#1d1d1d;
  --page:#f1f1f1;
  --white:#ffffff;
  --text:#2b2b2b;
  --muted:#6f6f6f;
  --rule:#cfcfcf;
}
*{box-sizing:border-box;margin:0;padding:0}
html,body{width:1200px;height:2529px;overflow:hidden}
body{position:relative;background:var(--page);font-family:"Open Sans",Arial,sans-serif;color:var(--text)}
.abs{position:absolute}

/* header */
.site-header{left:0;top:0;width:1200px;height:122px;background:var(--white)}
.brand{left:157px;top:12px;height:100px;display:flex;align-items:center;gap:18px}
.brand-mark{width:98px;height:98px;border-radius:50%;background:var(--gold)}
.brand-name{font-family:"Cabin",sans-serif;font-size:46px;font-weight:400;color:var(--gold)}
.main-nav{left:523px;top:46px;display:flex;align-items:center;font-size:16px;color:var(--text)}
.main-nav a{display:block;height:33px;line-height:33px;padding:0 18px;text-decoration:none;color:inherit}
.main-nav a.active{background:var(--gold);color:var(--white);border-radius:3px}
.search-icon{margin-left:10px}

/* hero */
.hero-photo{left:0;top:122px;width:1200px;height:477px;background:
  radial-gradient(ellipse 260px 200px at 260px 300px,#c9b5a3 0%,rgba(201,181,163,0) 100%),
  radial-gradient(ellipse 220px 180px at 560px 280px,#c7ab93 0%,rgba(199,171,147,0) 100%),
  radial-gradient(ellipse 240px 200px at 900px 250px,#d4bd9f 0%,rgba(212,189,159,0) 100%),
  linear-gradient(180deg,#e9e6e2 0%,#f4f2ef 55%,#dedad4 100%)}
.hero-band{left:0;top:599px;width:1200px;height:132px;background:var(--dark)}
.hero-tagline{left:152px;top:627px;width:480px;font-family:"Libre Baskerville",serif;font-size:25px;line-height:36px;color:var(--white)}
.hero-next{left:658px;top:640px}
.slider-arrow{top:330px;width:30px;height:66px;background:#9a9a9a;display:flex;align-items:center;justify-content:center}
.slider-arrow.left{left:0}
.slider-arrow.right{left:1170px}

.signup-box{left:728px;top:355px;width:315px;height:386px;background:var(--darker);padding:16px 15px}
.signup-box h2{font-family:"Cabin",sans-serif;font-weight:400;font-size:37px;line-height:40px;color:var(--white)}
.signup-box p{margin-top:8px;font-size:14px;line-height:19px;color:var(--white)}
.signup-box label{display:block;margin-top:12px;font-size:14px;color:var(--gold-light)}
.signup-box .field{margin-top:6px;height:38px;background:var(--white);border-radius:4px}
.signup-box .btn{margin-top:22px;height:40px;background:var(--gold);border-radius:4px;color:var(--white);font-family:"Cabin",sans-serif;font-size:24px;text-align:center;line-height:40px}

/* section headings */
.section-title{display:flex;align-items:center;font-family:"Cabin",sans-serif;font-weight:400;font-size:25px;color:var(--text);height:38px}
.section-title::before{content:"";width:6px;height:38px;background:var(--gold);margin-right:16px}
.section-title em{font-style:normal;color:var(--gold);margin-left:8px}
.section-title::after{content:"";height:2px;background:var(--gold);margin-left:18px}
.section-title.wide::after{width:120px}
.side-title{font-size:19px;height:32px}
.side-title::before{height:32px;margin-right:14px}
.side-title::after{width:70px}

/* posts */
.post-photo{left:155px;width:533px;height:355px;border-top:6px solid var(--gold)}
.post-photo.one{top:845px;background:
  radial-gradient(ellipse 140px 180px at 400px 200px,#c88b5f 0%,rgba(200,139,95,0) 100%),
  linear-gradient(90deg,#6d7073 0%,#b9bcbe 30%,#e6e4e0 55%,#f1ede8 100%)}
.post-photo.two{top:1504px;background:
  radial-gradient(ellipse 150px 170px at 170px 170px,#d3c2a6 0%,rgba(211,194,166,0) 100%),
  radial-gradient(ellipse 150px 180px at 380px 170px,#c49a74 0%,rgba(196,154,116,0) 100%),
  linear-gradient(90deg,#5d6b3f 0%,#8d8b62 45%,#6f7a45 100%)}
.post-lead{left:155px;width:533px;font-weight:700;font-size:16px;line-height:28px}
.post-excerpt{left:155px;width:533px;font-size:11.5px;line-height:16px;color:var(--muted)}
.post-excerpt b{color:var(--text);font-weight:700}
.comments-btn{left:155px;width:177px;height:48px;background:var(--gold);border-radius:4px;display:flex;align-items:center;gap:14px;padding-left:12px;color:var(--white);font-size:16px}
.divider{left:155px;width:533px;height:2px;background:var(--rule)}
.pager{left:155px;top:2088px;display:flex;gap:12px;font-size:15px}
.pager span{display:flex;align-items:center;gap:8px;height:28px;padding:0 12px;border-radius:3px}
.pager .prev{background:var(--dark);color:var(--white)}
.pager .next{background:#dcdcdc;color:#b5b5b5}

/* sidebar */
.side-card{left:728px;width:315px;border-top:6px solid var(--gold)}
.side-card .caption{position:absolute;left:0;bottom:0;width:100%;padding:10px;background:rgba(30,30,30,.55);color:var(--white);font-size:13px;font-weight:700;line-height:17px;text-align:center}
.side-text{left:728px;width:315px;font-size:13.5px;font-weight:700;line-height:20px}
.side-text a{color:var(--gold);text-decoration:none}
.praise-box{left:728px;top:1507px;width:315px;height:208px;border:1px solid var(--rule);border-top:6px solid var(--gold);background:var(--white);padding:34px 14px 0}
.praise-box p{font-size:12px;line-height:19px;text-align:justify}
.praise-box .by{margin-top:6px;text-align:right;color:var(--gold);font-weight:700;font-size:12px}
.praise-nav{position:absolute;right:12px;top:8px;display:flex;gap:6px}
.poster{width:80px;height:122px;border:3px solid #f4ecd8;box-shadow:0 2px 5px rgba(0,0,0,.35)}
.poster.p1{left:762px;top:1800px;transform:rotate(-9deg);background:linear-gradient(180deg,#d9b24a 0%,#c8893a 55%,#7d5a2c 100%)}
.poster.p2{left:847px;top:1796px;transform:rotate(-2deg);background:linear-gradient(180deg,#e7c46a 0%,#c5573a 55%,#3a3a3a 100%)}
.poster.p3{left:932px;top:1802px;transform:rotate(8deg);background:linear-gradient(180deg,#f0d77e 0%,#d9a640 55%,#2e2a26 100%)}
.link-list{left:728px;top:2012px;width:315px;height:203px;border:1px solid var(--rule);border-top:6px solid var(--gold);background:var(--white);padding:16px 12px;list-style:none}
.link-list li{display:flex;align-items:center;gap:10px;height:25px;font-size:12px}

/* footer */
.site-footer{left:0;top:2243px;width:1200px;height:238px;background:var(--dark);border-top:6px solid var(--gold)}
.footer-title{display:flex;align-items:center;font-family:"Cabin",sans-serif;font-weight:400;font-size:20px;color:var(--white)}
.footer-title::before{content:"";width:5px;height:32px;background:var(--gold);margin-right:14px}
.footer-title::after{content:"";width:70px;height:2px;background:var(--gold);margin-left:14px}
.footer-title em{font-style:normal;color:var(--gold);margin-left:6px}
.footer-about{left:155px;top:2345px;width:290px;font-size:12px;line-height:16px;color:#9b9b9b;text-align:justify}
.events{left:497px;top:2340px;list-style:none;font-size:12px;line-height:22px;color:#cfcfcf}
.events li::before{content:"› ";color:var(--gold)}
.newsletter-text{left:779px;top:2340px;width:290px;font-size:12px;font-weight:700;line-height:18px;color:#cfcfcf}
.newsletter-form{left:779px;top:2385px;width:246px;height:28px;background:var(--white);border-radius:14px;overflow:hidden}
.newsletter-form span{position:absolute;right:0;top:0;width:72px;height:28px;background:var(--gold);color:var(--white);font-size:12px;font-weight:700;text-align:center;line-height:28px}
.legal-bar{left:0;top:2481px;width:1200px;height:48px;background:#e6e6e6;display:flex;justify-content:center;align-items:center;font-size:11px;color:var(--muted)}
</style>
</head>
<body>

<header class="abs site-header">
  <div class="abs brand"><div class="brand-mark"></div><span class="brand-name">Pelorn</span></div>
  <nav class="abs main-nav">
    <a class="active" href="#">HOME</a><a href="#">ABOUT US</a><a href="#">WORK WITH ME</a><a href="#">PRAISE</a><a href="#">GIVING BACK</a>
    <svg class="search-icon" width="18" height="18" viewBox="0 0 18 18"><circle cx="7" cy="7" r="5.5" fill="none" stroke="#a97c4f" stroke-width="2.2"/><line x1="11" y1="11" x2="16" y2="16" stroke="#a97c4f" stroke-width="2.4"/></svg>
  </nav>
</header>

<div class="abs hero-photo" role="img" aria-label="Smiling family of four relaxing together on a white sofa in a bright living room"></div>
<div class="abs slider-arrow left"><svg width="14" height="24" viewBox="0 0 14 24"><path d="M11 2 3 12l8 10" fill="none" stroke="#fff" stroke-width="3"/></svg></div>
<div class="abs slider-arrow right"><svg width="14" height="24" viewBox="0 0 14 24"><path d="M3 2l8 10-8 10" fill="none" stroke="#fff" stroke-width="3"/></svg></div>
<div class="abs hero-band"></div>
<p class="abs hero-tagline">Quis nostrud exerci tation ullamcorper suscipit</p>
<svg class="abs hero-next" width="54" height="54" viewBox="0 0 54 54"><circle cx="27" cy="27" r="24" fill="none" stroke="#a97c4f" stroke-width="3"/><path d="M23 17l10 10-10 10" fill="none" stroke="#a97c4f" stroke-width="3.5"/></svg>

<section class="abs signup-box">
  <h2>Hendrerit in vulputate velit</h2>
  <p>sit amet, consectass etuer adipiscing elit, sed diam nonummy.</p>
  <label>Name:</label><div class="field"></div>
  <label>Email:</label><div class="field"></div>
  <div class="btn">Get it!</div>
</section>

<!-- posts -->
<h3 class="abs section-title wide" style="left:155px;top:783px">Consectetuer <em>Adipiscing elit</em></h3>
<div class="abs post-photo one" role="img" aria-label="Smiling woman working at a desktop computer in an office"></div>
<p class="abs post-lead" style="top:1211px">Lorem ipsum dolor sit amet, consectetuer adipiscing elit sed diam nonummy</p>
<p class="abs post-excerpt" style="top:1282px">Uis nostrud exerci tation ullamcorper suscipit lobortis nisl ut aliquip ex ea commodo consequat. Duis autem vel eum iriure dolor in hendrerit in vulputate velit esse molestie consequat, vel illum dolore eu feugiat nulla facilisis. <b>› KEEP READING</b></p>
<div class="abs comments-btn" style="top:1345px"><svg width="34" height="30" viewBox="0 0 34 30"><rect x="2" y="2" width="26" height="20" rx="3" fill="none" stroke="#fff" stroke-width="2"/><path d="M8 22l-2 6 8-6" fill="none" stroke="#fff" stroke-width="2"/><line x1="8" y1="9" x2="22" y2="9" stroke="#fff" stroke-width="2"/><line x1="8" y1="15" x2="18" y2="15" stroke="#fff" stroke-width="2"/></svg>78 Comments</div>
<div class="abs divider" style="top:1420px"></div>

<h3 class="abs section-title wide" style="left:155px;top:1445px">Vulputate velit <em>Molestie</em></h3>
<div class="abs post-photo two" role="img" aria-label="Mother and grown daughter laughing together outdoors"></div>
<p class="abs post-lead" style="top:1873px">Lorem ipsum dolor sit amet, consectetuer adipiscing elit sed diam nonummy</p>
<p class="abs post-excerpt" style="top:1946px">Uis nostrud exerci tation ullamcorper suscipit lobortis nisl ut aliquip ex ea commodo consequat. Duis autem vel eum iriure dolor in hendrerit in vulputate velit esse molestie consequat, vel illum dolore eu feugiat nulla. <b>› KEEP READING</b></p>
<div class="abs comments-btn" style="top:2007px"><svg width="34" height="30" viewBox="0 0 34 30"><rect x="2" y="2" width="26" height="20" rx="3" fill="none" stroke="#fff" stroke-width="2"/><path d="M8 22l-2 6 8-6" fill="none" stroke="#fff" stroke-width="2"/><line x1="8" y1="9" x2="22" y2="9" stroke="#fff" stroke-width="2"/><line x1="8" y1="15" x2="18" y2="15" stroke="#fff" stroke-width="2"/></svg>21 Comments</div>
<div class="abs divider" style="top:2074px"></div>
<div class="abs pager"><span class="prev"><svg width="14" height="14" viewBox="0 0 14 14"><circle cx="7" cy="7" r="6" fill="none" stroke="#fff"/><path d="M8 4 5 7l3 3" fill="none" stroke="#fff" stroke-width="1.5"/></svg>Previous Entries</span><span class="next">Next Entries</span></div>

<!-- sidebar -->
<h3 class="abs section-title side-title" style="left:728px;top:786px">Consectetuer <em>Adipiscing elit</em></h3>
<div class="abs side-card" style="top:845px;height:226px;background:radial-gradient(ellipse 70px 90px at 90px 100px,#c9a889 0%,rgba(201,168,137,0) 100%),radial-gradient(ellipse 70px 90px at 220px 100px,#d0ad8c 0%,rgba(208,173,140,0) 100%),linear-gradient(90deg,#4f5c33,#8a8a60 50%,#5d6a3d)" role="img" aria-label="Two women laughing together outdoors"><div class="caption">QUIS NOSTRUD EXERCI TATION</div></div>
<p class="abs side-text" style="top:1082px">Lorem ipsum dolor sit amet, consectetuer adipiscing elit sed diam nonummy <a href="#">Read More</a></p>

<h3 class="abs section-title side-title" style="left:728px;top:1154px">Resources</h3>
<div class="abs side-card" style="top:1205px;height:228px;background:radial-gradient(ellipse 60px 80px at 120px 100px,#b88d6c 0%,rgba(184,141,108,0) 100%),radial-gradient(ellipse 70px 90px at 220px 110px,#cfc6bc 0%,rgba(207,198,188,0) 100%),linear-gradient(90deg,#3f342b,#7a6552 50%,#4b3d31)" role="img" aria-label="Young family with a small child at home in a kitchen"><div class="caption">IRIURE DOLOR IN HENDRERIT IN VULPUTATE VELIT ESSE MOLESTIE</div></div>

<h3 class="abs section-title side-title" style="left:728px;top:1463px">Praise</h3>
<section class="abs praise-box">
  <div class="praise-nav">
    <svg width="16" height="16" viewBox="0 0 16 16"><circle cx="8" cy="8" r="7" fill="none" stroke="#333"/><path d="M9.5 4.5 6 8l3.5 3.5" fill="none" stroke="#333" stroke-width="1.5"/></svg>
    <svg width="16" height="16" viewBox="0 0 16 16"><circle cx="8" cy="8" r="7" fill="none" stroke="#333"/><path d="M6.5 4.5 10 8l-3.5 3.5" fill="none" stroke="#333" stroke-width="1.5"/></svg>
  </div>
  <p>"Lorem ipsum dolor sit amet, consectetuer adipiscing elit, sed diam nonummy nibh euismod tincidunt ut laoreet dolore magna aliquam erat volutpat. Ut wisi enim ad minim veniam, quis nostrud exerci tation ullamcorper suscipit lobortis nisl ut laoreet dolore magna aliquam, quis nostrud exerc."</p>
  <div class="by">-Exercitation Ullamcorpe</div>
</section>

<h3 class="abs section-title side-title" style="left:728px;top:1745px">Consectetuer <em>Adipiscing elit</em></h3>
<div class="abs poster p1" role="img" aria-label="Vintage champagne poster"></div>
<div class="abs poster p2" role="img" aria-label="Vintage champagne poster"></div>
<div class="abs poster p3" role="img" aria-label="Vintage champagne poster"></div>

<h3 class="abs section-title side-title" style="left:728px;top:1963px">Consectetuer <em>Adipiscing elit</em></h3>
<ul class="abs link-list">
  <li><svg width="14" height="14" viewBox="0 0 14 14"><circle cx="7" cy="7" r="6" fill="none" stroke="#333"/><path d="M6 4l3 3-3 3" fill="none" stroke="#333" stroke-width="1.4"/></svg>Lorem ipsum dolor sit amet</li>
  <li><svg width="14" height="14" viewBox="0 0 14 14"><circle cx="7" cy="7" r="6" fill="none" stroke="#333"/><path d="M6 4l3 3-3 3" fill="none" stroke="#333" stroke-width="1.4"/></svg>Dolor in hendrerit in vulputate ipsum</li>
  <li><svg width="14" height="14" viewBox="0 0 14 14"><circle cx="7" cy="7" r="6" fill="none" stroke="#333"/><path d="M6 4l3 3-3 3" fill="none" stroke="#333" stroke-width="1.4"/></svg>Nostrud exerci tation</li>
  <li><svg width="14" height="14" viewBox="0 0 14 14"><circle cx="7" cy="7" r="6" fill="none" stroke="#333"/><path d="M6 4l3 3-3 3" fill="none" stroke="#333" stroke-width="1.4"/></svg>vulputate velit esse molestie</li>
  <li><svg width="14" height="14" viewBox="0 0 14 14"><circle cx="7" cy="7" r="6" fill="none" stroke="#333"/><path d="M6 4l3 3-3 3" fill="none" stroke="#333" stroke-width="1.4"/></svg>Endrerit in vulputate velit</li>
  <li><svg width="14" height="14" viewBox="0 0 14 14"><circle cx="7" cy="7" r="6" fill="none" stroke="#333"/><path d="M6 4l3 3-3 3" fill="none" stroke="#333" stroke-width="1.4"/></svg>tation ullamcorper suscipit lob</li>
</ul>

<!-- footer -->
<footer class="abs site-footer"></footer>
<h4 class="abs footer-title" style="left:155px;top:2286px">About <em>Pelorn</em></h4>
<p class="abs footer-about">Lorem ipsum dolor sit amet, consectetuer adipiscing elit, sed diam nonummy nibh euismod tincidunt ut laoreet dolore magna aliquam erat volutpat. Ut wisi enim ad minim veniam, quis nostrud exerci tation ullamcorper suscipit lobortis nisl ut aliquip ex ea commodo consequat duis autem vel eum iriure dolor in hendrerit.</p>
<h4 class="abs footer-title" style="left:497px;top:2286px">Upcoming Events</h4>
<ul class="abs events">
  <li>Lorem ipsum dolor sit amet</li>
  <li>consectetuer adipiscing elit, sed diam</li>
  <li>nonummy nibh euismod tincidunt</li>
  <li>laoreet dolore magna aliquam erat</li>
  <li>volutpat minim veniam ostrud exerci tation</li>
  <li>eros et accumsan et iusto odio dignissim</li>
</ul>
<h4 class="abs footer-title" style="left:779px;top:2286px">Newsletter Signup</h4>
<p class="abs newsletter-text">Lorem ipsum dolor sit amet, consectetuer adipiscing elit, sed diam nonummy nibh</p>
<div class="abs newsletter-form"><span>JOIN US</span></div>
<div class="abs legal-bar">Privacy Policy &nbsp;|&nbsp; © 2014 Pelorn &nbsp;|&nbsp; Terms Policy &nbsp;|&nbsp; Disclaimer</div>

</body>
</html>
```